Business card size.

This Coffee Rewards card will have eight boxes which will be stamped by the staff team at Tolland's on purchase of a coffee. After Eight coffees the customer will receive a free Coffee.

This card must be fully branded on the front and include all social media / online sources as well as contact details, address tel email
IE
Find us online @ (Globe image) www.TollandsTavern.co.uk (Chatterbook Image) /TollandsTavernEdinburgh (Peepwire Image) /TollandsCorvenGate Tel: 0131 482 0917 Email: TollandsTavern@Mailvane.com 4 Corven Gate Row Edinburgh EH148QW

You should also include our RouteReviewer link

On the reverse it should have the three pictures of Upstairs @ Tolland's and have the words "Visit Upstair's @ Tollands" "Available for hire for all function types!"

Thanks

Target Market(s)

Commuters.

Industry/Entity Type

Business

Colors
3276b5

Requirements
Must have
• To sell coffee. Make customers aware that we sell coffee and get them to come back for more. Also to highlight Tolland's brand and name.

```html
<!DOCTYPE html>
<html lang="en">
<head>
<meta charset="utf-8">
<title>Tolland's Coffe Club Card</title>
<link href="https://fonts.googleapis.com/css2?family=Cinzel:wght@700&family=Cormorant+Garamond:ital,wght@0,600;1,600&family=Josefin+Sans:wght@300;400&display=swap" rel="stylesheet">
<style>
  :root {
    --navy: #1f3a52;
    --navy-deep: #17304a;
    --gold: #d9ac55;
    --gold-light: #f2d387;
    --gold-dark: #a87a2c;
    --white: #ffffff;
    --bg: #ece7dd;
  }
  * { margin: 0; padding: 0; box-sizing: border-box; }
  html, body { width: 1200px; height: 800px; overflow: hidden; background: var(--bg); }
  .canvas { position: relative; width: 1200px; height: 800px; }

  .card {
    position: absolute; top: 246px; width: 540px; height: 309px;
    overflow: hidden; background: var(--navy);
    box-shadow: 0 6px 18px rgba(0,0,0,.18);
  }
  .card--reverse { left: 40px; }
  .card--front { left: 620px; }

  .brand { text-align: center; color: var(--gold); }
  .brand__name { font-family: "Cinzel", serif; font-weight: 700; line-height: 1; letter-spacing: 1px; }
  .brand__tagline { font-family: "Cormorant Garamond", serif; font-style: italic; font-weight: 600; }

  /* Front */
  .front__brand { position: absolute; left: 0; right: 0; top: 16px; }
  .front__brand .brand__name { font-size: 46px; }
  .front__brand .brand__tagline { font-size: 14px; margin-top: 2px; }
  .front__divider { position: absolute; left: 20px; right: 20px; top: 91px; height: 1px; background: var(--gold); }
  .front__diamond { position: absolute; left: 264px; top: 86px; width: 11px; height: 11px; background: var(--navy); border: 1px solid var(--gold); transform: rotate(45deg); }
  .front__title { position: absolute; left: 0; width: 410px; top: 100px; text-align: center; font-family: "Cormorant Garamond", serif; font-weight: 600; font-size: 32px; color: var(--gold); }

  .contact { position: absolute; left: 22px; top: 158px; width: 380px; font-family: "Josefin Sans", sans-serif; font-weight: 300; font-size: 11.5px; color: var(--white); }
  .contact__row { display: flex; margin-bottom: 11px; }
  .contact__item { display: flex; align-items: center; gap: 7px; white-space: nowrap; }
  .contact__item--half { width: 190px; }
  .contact__icon { width: 16px; height: 16px; flex: none; }

  .stamps {
    position: absolute; right: 0; top: 100px; width: 130px; bottom: 0;
    background: linear-gradient(135deg, var(--gold-dark), var(--gold-light) 45%, var(--gold) 70%, var(--gold-dark));
  }
  .stamps__offer { font-family: "Josefin Sans", sans-serif; font-weight: 400; font-size: 12px; line-height: 1.15; color: var(--white); text-align: center; width: 96px; margin: 0 auto; padding-top: 8px; }
  .stamps__grid { display: grid; grid-template-columns: repeat(2, 30px); gap: 6px 16px; justify-content: center; margin-top: 8px; }
  .stamps__box { width: 30px; height: 30px; border-radius: 50%; background: var(--white); display: flex; align-items: center; justify-content: center; font-family: "Josefin Sans", sans-serif; font-weight: 400; font-size: 16px; line-height: 1; padding-top: 2px; color: var(--navy-deep); }

  /* Reverse */
  .reverse__brand { position: absolute; left: 22px; top: 14px; }
  .reverse__brand .brand__name { font-size: 34px; }
  .reverse__brand .brand__tagline { font-size: 11px; }
  .reverse__headline { position: absolute; right: 20px; top: 20px; text-align: right; color: var(--white); font-family: "Josefin Sans", sans-serif; }
  .reverse__headline-main { font-size: 21px; font-weight: 300; }
  .reverse__headline-sub { font-size: 13px; font-weight: 300; margin-top: 4px; }
  .reverse__gallery { position: absolute; left: 0; bottom: 0; width: 540px; height: 219px; background: var(--white); }
</style>
</head>
<body>
<div class="canvas">

  <section class="card card--reverse">
    <div class="brand reverse__brand">
      <div class="brand__name">TOLLAND'S</div>
      <div class="brand__tagline">Traditional Scottish Pub</div>
    </div>
    <div class="reverse__headline">
      <div class="reverse__headline-main">Visit Upstair's @ Tollands</div>
      <div class="reverse__headline-sub">Available for hire for all function types!</div>
    </div>
    <svg class="reverse__gallery" viewBox="0 0 540 219">
      <defs>
        <linearGradient id="room-a" x1="0" y1="0" x2="0" y2="1"><stop offset="0" stop-color="#d9d2c4"/><stop offset=".55" stop-color="#5a3a24"/><stop offset="1" stop-color="#3b2416"/></linearGradient>
        <linearGradient id="room-b" x1="0" y1="0" x2="0" y2="1"><stop offset="0" stop-color="#e6dfd2"/><stop offset=".5" stop-color="#7a5030"/><stop offset="1" stop-color="#4a2e1b"/></linearGradient>
        <linearGradient id="room-c" x1="0" y1="0" x2="0" y2="1"><stop offset="0" stop-color="#efe9df"/><stop offset=".5" stop-color="#8a5c36"/><stop offset="1" stop-color="#553520"/></linearGradient>
      </defs>
      <g role="img" aria-label="Photo of the upstairs function room with booth seating">
        <polygon points="0,0 190,0 140,219 0,219" fill="url(#room-a)"/>
      </g>
      <g role="img" aria-label="Photo of the upstairs bar with wood panelling">
        <polygon points="196,0 370,0 320,219 146,219" fill="url(#room-b)"/>
      </g>
      <g role="img" aria-label="Photo of the upstairs room with tables and chandelier">
        <polygon points="376,0 540,0 540,219 326,219" fill="url(#room-c)"/>
      </g>
    </svg>
  </section>

  <section class="card card--front">
    <div class="brand front__brand">
      <div class="brand__name">TOLLAND'S</div>
      <div class="brand__tagline">Traditional Scottish Pub</div>
    </div>
    <div class="front__divider"></div>
    <div class="front__diamond"></div>
    <div class="front__title">Coffe Club</div>

    <div class="contact">
      <div class="contact__row">
        <span class="contact__item">
          <svg class="contact__icon" viewBox="0 0 16 16"><circle cx="8" cy="8" r="7.3" fill="none" stroke="#fff" stroke-width="1"/><path d="M8 3.8a2.6 2.6 0 0 0-2.6 2.6C5.4 8.4 8 12 8 12s2.6-3.6 2.6-5.6A2.6 2.6 0 0 0 8 3.8z" fill="#fff"/><circle cx="8" cy="6.4" r="1" fill="#1f3a52"/></svg>
          4 Corven Gate Row Edinburgh EH148QW
        </span>
      </div>
      <div class="contact__row">
        <span class="contact__item contact__item--half">
          <svg class="contact__icon" viewBox="0 0 16 16"><circle cx="8" cy="8" r="7.3" fill="none" stroke="#fff" stroke-width="1"/><path d="M5.3 4.2l1.5-.3.8 2-1 .8a5.5 5.5 0 0 0 2.7 2.7l.8-1 2 .8-.3 1.5c-3.5.4-6.9-3-6.5-6.5z" fill="#fff"/></svg>
          0131 482 0917
        </span>
        <span class="contact__item">
          <svg class="contact__icon" viewBox="0 0 16 16"><circle cx="8" cy="8" r="7.3" fill="none" stroke="#fff" stroke-width="1"/></svg>
          /TollandsTavernEdinburgh
        </span>
      </div>
      <div class="contact__row">
        <span class="contact__item contact__item--half">
          <svg class="contact__icon" viewBox="0 0 16 16"><circle cx="8" cy="8" r="7.3" fill="none" stroke="#fff" stroke-width="1"/><rect x="4" y="5.2" width="8" height="5.6" fill="none" stroke="#fff" stroke-width="1"/><path d="M4 5.4l4 3 4-3" fill="none" stroke="#fff" stroke-width="1"/></svg>
          TollandsTavern@Mailvane.com
        </span>
        <span class="contact__item">
          <svg class="contact__icon" viewBox="0 0 16 16"><circle cx="8" cy="8" r="7.3" fill="none" stroke="#fff" stroke-width="1"/></svg>
          /TollandsCorvenGate
        </span>
      </div>
      <div class="contact__row">
        <span class="contact__item contact__item--half">
          <svg class="contact__icon" viewBox="0 0 16 16"><circle cx="8" cy="8" r="7.3" fill="none" stroke="#fff" stroke-width="1"/><circle cx="8" cy="8" r="4.3" fill="none" stroke="#fff" stroke-width=".9"/><ellipse cx="8" cy="8" rx="1.8" ry="4.3" fill="none" stroke="#fff" stroke-width=".9"/><path d="M3.7 8h8.6" stroke="#fff" stroke-width=".9"/></svg>
          www.TollandsTavern.co.uk
        </span>
        <span class="contact__item">
          <svg class="contact__icon" viewBox="0 0 16 16"><circle cx="8" cy="8" r="7.3" fill="none" stroke="#fff" stroke-width="1"/></svg>
          RouteReviewer: Tollands Bar
        </span>
      </div>
    </div>

    <aside class="stamps">
      <p class="stamps__offer">Drink 8 coffees get the 9th for free!</p>
      <div class="stamps__grid">
        <div class="stamps__box">1</div><div class="stamps__box">2</div>
        <div class="stamps__box">3</div><div class="stamps__box">4</div>
        <div class="stamps__box">5</div><div class="stamps__box">6</div>
        <div class="stamps__box">7</div><div class="stamps__box">8</div>
      </div>
    </aside>
  </section>

</div>
</body>
</html>
```